Postcard Design Project

Real Estate agent, seeking new listings in an area where there is a short supply. My offer is that I will sell a home in under 60 days or I pay the owners mortgage until I do sell it.

```html
<!DOCTYPE html>
<html lang="en">
<head>
<meta charset="utf-8">
<title>Postcard – 60 Day Sale Guarantee</title>
<link href="https://fonts.googleapis.com/css2?family=Mulish:wght@400;600;700;800;900&display=swap" rel="stylesheet">
<style>
  :root {
    --stage: #1c1c1c;
    --stage-edge: #3a3a3a;
    --blue-top: #0a58a6;
    --blue-mid: #0d4a97;
    --blue-bottom: #2a2f86;
    --ink-black: #0b0b0c;
    --white: #ffffff;
    --gold: #f6b418;
    --gold-light: #ffd34a;
    --orange: #f39a12;
    --orange-deep: #e9850b;
    --yellow-text: #f3e13a;
    --band-text: #1b1b1b;
    --paper: #f4f4f4;
    --stamp: #c9c9c9;
    --navy: #1b2f66;
  }
  * { box-sizing: border-box; margin: 0; padding: 0; }
  html, body { width: 1200px; height: 604px; overflow: hidden; }
  body {
    background: var(--stage);
    border: 1px solid var(--stage-edge);
    font-family: "Mulish", "Century Gothic", sans-serif;
    position: relative;
  }
  .card { position: absolute; top: 116px; width: 483px; height: 372px; overflow: hidden; }
  .card-front { left: 102px; background: var(--ink-black); }
  .card-back { left: 614px; background: var(--paper); }

  /* Front – headline panel */
  .offer {
    position: absolute; left: 0; top: 0; width: 100%; height: 184px;
    background: linear-gradient(180deg, var(--blue-top) 0%, var(--blue-mid) 45%, var(--blue-bottom) 100%);
    text-align: center; color: var(--white);
  }
  .offer-headline {
    padding-top: 22px;
    font-size: 28px; font-weight: 700; line-height: 36px; letter-spacing: -0.2px;
  }
  .accent {
    font-weight: 900;
    background: linear-gradient(180deg, var(--gold-light) 0%, var(--gold) 55%, var(--orange-deep) 100%);
    -webkit-background-clip: text; background-clip: text; color: transparent;
  }
  .offer-promise { margin-top: 6px; font-size: 17px; font-weight: 800; }
  .offer-promise .gold { color: var(--gold); }
  .offer-fineprint {
    position: absolute; right: 49px; top: 160px; font-size: 7px; font-weight: 700;
  }

  /* Front – brand & contact */
  .brand-tile {
    position: absolute; left: 20px; top: 225px; width: 93px; height: 76px;
    background: var(--white); border-radius: 4px;
    display: flex; flex-direction: column; align-items: center; justify-content: center; gap: 6px;
    color: var(--navy); font-weight: 800; font-size: 11px; line-height: 13px; text-align: center;
  }
  .brand-tile .brand-mark { width: 14px; height: 14px; background: var(--navy); }
  .contact { position: absolute; left: 136px; top: 213px; list-style: none; color: var(--white); font-size: 11.5px; }
  .contact li { display: flex; align-items: center; height: 19.2px; }
  .contact svg { width: 11px; height: 11px; margin-right: 10px; flex: none; }
  .contact .no-icon { padding-left: 21px; }
  .website { position: absolute; left: 136px; top: 296px; color: var(--gold); font-size: 11.5px; font-weight: 800; }

  .agent-photo {
    position: absolute; left: 341px; top: 184px; width: 142px; height: 188px;
    background: linear-gradient(160deg, #a0623a 0%, #7a4323 45%, #5c321b 75%, #a9c7d6 100%);
  }
  .badge-band {
    position: absolute; left: 0; top: 336px; width: 341px; height: 36px;
    background: linear-gradient(180deg, var(--gold-light) 0%, var(--orange) 100%);
    color: var(--band-text); font-size: 13px; font-weight: 900;
    padding-left: 22px; line-height: 36px;
  }

  /* Back */
  .message {
    position: absolute; left: 0; top: 0; width: 377px; height: 122px;
    background: linear-gradient(180deg, var(--blue-top) 0%, var(--blue-mid) 55%, var(--blue-bottom) 100%);
    color: var(--white); padding: 17px 20px 0 21px;
  }
  .message-body { font-size: 8.6px; font-weight: 800; line-height: 11.4px; text-align: justify; }
  .message-cta { margin-top: 9px; text-align: center; color: var(--yellow-text); font-size: 12px; font-weight: 800; line-height: 19px; }
  .phone-pill {
    display: inline-flex; align-items: center; gap: 5px; vertical-align: middle;
    height: 20px; padding: 0 10px 0 5px; border-radius: 10px;
    background: linear-gradient(180deg, var(--gold-light), var(--orange-deep));
    color: var(--band-text); font-size: 11px; font-weight: 800;
  }
  .phone-pill svg { width: 13px; height: 13px; }
  .stamp-box {
    position: absolute; left: 392px; top: 26px; width: 78px; height: 79px;
    background: var(--stamp); color: #222; font-size: 13.5px; line-height: 17px;
    display: flex; align-items: center; justify-content: center; text-align: center;
  }
</style>
</head>
<body>
  <section class="card card-front">
    <div class="offer">
      <h1 class="offer-headline">
        I <span class="accent">GUARANTEE</span> that<br>
        I will sell your home in<br>
        <span class="accent">60 DAYS</span> or less
      </h1>
      <p class="offer-promise">or I will <span class="gold">PAY YOUR MORTGAGE UNTIL I DO</span>*</p>
      <p class="offer-fineprint">*certain conditions apply</p>
    </div>

    <div class="brand-tile">
      <span class="brand-mark"></span>
      <span>HARBORLINE<br>REALTY</span>
    </div>

    <ul class="contact">
      <li>
        <svg viewBox="0 0 12 12"><path fill="#f6b418" d="M1 4.5C1 3 3 2 6 2s5 1 5 2.5L9.5 5 8.5 4H3.5l-1 1zM3 6h6l1.5 4.5h-9z"/></svg>
        (555) 014-2380
      </li>
      <li>
        <svg viewBox="0 0 12 12"><rect x="1" y="3" width="10" height="7" fill="#f6b418"/><path d="M1 3l5 4 5-4" stroke="#0b0b0c" fill="none"/></svg>
        dana@harborlinerealty.com
      </li>
      <li>
        <svg viewBox="0 0 12 12"><path fill="#f6b418" d="M6 0.5a4 4 0 0 1 4 4c0 3-4 7-4 7s-4-4-4-7a4 4 0 0 1 4-4z"/><circle cx="6" cy="4.5" r="1.5" fill="#0b0b0c"/></svg>
        1180 Harbor View Rd #204
      </li>
      <li class="no-icon">Wilmington NC 28400</li>
    </ul>
    <p class="website">www.seaportsbestagent.com</p>

    <div class="badge-band">WILMINGTONS 5 STAR HOMEFINDER PREMIER AGENT</div>
    <div class="agent-photo" role="img" aria-label="Photo of a toddler on a wooden deck holding the agent's name-and-phone sign, with a For Sale sign below"></div>
  </section>

  <section class="card card-back">
    <div class="message">
      <p class="message-body">Hurricane Florence has affected thousands of homes in Wilmington, and as a result we have a backlog of buyers ready to make good offers on homes right now. Allow me to help you sell your home for the most amount of money, in the least amount of time.</p>
      <p class="message-cta">
        Call me today for a customized Home Valuation<br>
        specific to your home
        <span class="phone-pill">
          <svg viewBox="0 0 14 14"><circle cx="7" cy="7" r="7" fill="#1b1b1b"/><path fill="#f6b418" d="M4.2 3.5l1.6-.3.8 2-1 .7a6 6 0 0 0 2.5 2.5l.7-1 2 .8-.3 1.6c-3.5.3-6.6-2.8-6.3-6.3z"/></svg>
          555-014-2380
        </span>
      </p>
    </div>
    <div class="stamp-box">Stamp<br>Here</div>
  </section>
</body>
</html>
```